Advertisement Design Project

We need to design a backdrop and 2 roll up banners and table skirts for tradeshow displays...We have a current logo design and a basic idea how we need the artwork too look....need a designer to put it all together!!

Target Market(s)

Our target is mostly women...Its for the canadian and american market!!

Requirements
Must have
• What VOLARI means is "free" to be free....freedom!!!!
Need to have a good vision of what a final display for trade shows should look like!!
attractive colours..not too bold....clean but fun look!!!!
-express your individuality
-interchangeable
-create your own style
-Designed by you
-endless possibilities
Nice to have
• -freedom to express your own style
-butterflies
-Birds
-colourful
websites that have similar product line
www.tasperinjewelry.example
www.brolfjewelry.example
www.quibel-dornholt.example

Should not have
• No Direct infringement to the sites listed above!!!

```html
<!DOCTYPE html>
<html lang="en">
<head>
<meta charset="utf-8">
<title>Volari Collection – Trade Show Display</title>
<link rel="stylesheet" href="https://fonts.googleapis.com/css2?family=Oswald:wght@500;700&family=Lato:wght@400;700&display=swap">
<style>
  :root {
    --page-bg: #e4e4e6;
    --panel-white: #fbf9f8;
    --panel-cream: #f4eeec;
    --ink: #1c1c1c;
    --magenta: #c2368f;
    --magenta-deep: #a02c86;
    --purple: #7e3a9e;
    --blush: #f2d6e6;
    --peach: #f3d9cf;
    --teal-soft: #93c9c6;
    --sky: #27a8e0;
    --coral: #e4523f;
    --display: "Oswald", "Arial Narrow", sans-serif;
    --text: "Lato", "Helvetica Neue", Arial, sans-serif;
  }
  * { box-sizing: border-box; margin: 0; padding: 0; }
  html, body { width: 1200px; height: 849px; overflow: hidden; }
  body { background: var(--page-bg); font-family: var(--text); color: var(--ink); position: relative; }

  .brand { text-align: center; font-family: var(--text); font-weight: 400; color: var(--ink); line-height: 1; }
  .brand__name { display: block; }
  .brand__sub { display: block; }

  /* Backdrop */
  .backdrop {
    position: absolute; left: 250px; top: 110px; width: 700px; height: 430px;
    background: linear-gradient(180deg, var(--panel-white) 0%, var(--panel-cream) 100%);
    overflow: hidden;
  }
  .backdrop .brand { position: absolute; left: 0; right: 0; top: 40px; }
  .backdrop .brand__name { font-size: 64px; letter-spacing: 1px; }
  .backdrop .brand__sub { font-size: 26px; margin-top: 4px; }
  .backdrop__art {
    position: absolute; right: -40px; bottom: -40px; width: 560px; height: 320px;
    background: radial-gradient(ellipse at 40% 70%, rgba(194,54,143,.55) 0%, rgba(233,170,190,.45) 40%, rgba(243,217,207,.3) 65%, rgba(244,238,236,0) 80%);
  }
  .tagline { position: absolute; left: 60px; top: 200px; font-family: var(--display); font-weight: 700; line-height: 1.05; white-space: nowrap; }
  .tagline__lead { display: block; font-size: 40px; color: var(--ink); }
  .tagline__rest { display: block; font-size: 22px; color: var(--ink); }
  .tagline__accent { color: var(--magenta); }

  /* Roll-up banners */
  .rollup {
    position: absolute; top: 120px; width: 170px; height: 560px;
    background: var(--panel-white); overflow: hidden;
  }
  .rollup--left { left: 50px; }
  .rollup--right { left: 980px; }
  .rollup .brand { margin-top: 40px; }
  .rollup .brand__name { font-size: 40px; }
  .rollup .brand__sub { font-size: 15px; margin-top: 2px; }

  .rollup__swirl {
    position: absolute; left: 0; top: 120px; width: 100%; height: 120px;
    background: linear-gradient(160deg, rgba(242,214,230,0) 0%, rgba(242,214,230,.9) 50%, rgba(242,214,230,0) 100%);
  }
  .rollup__product {
    position: absolute; left: 18px; top: 230px; width: 134px; height: 46px; border-radius: 10px;
    background: linear-gradient(90deg, #e9e5df 0%, #cfd8c8 50%, #e0e6ea 100%);
  }
  .rollup__note { position: absolute; left: 14px; top: 300px; font-weight: 700; font-size: 17px; color: var(--teal-soft); }
  .rollup__circles {
    position: absolute; left: 0; bottom: 70px; width: 100%; height: 150px;
    background: radial-gradient(circle at 20% 60%, rgba(194,54,143,.18) 0%, rgba(194,54,143,0) 60%);
  }
  .rollup__closing { position: absolute; left: 10px; right: 6px; bottom: 24px; font-family: var(--display); line-height: 1.15; white-space: nowrap; }
  .rollup__closing > span { display: block; }
  .rollup__closing .small { font-size: 14px; font-weight: 500; }
  .rollup__closing .big { font-size: 19px; font-weight: 700; }
  .rollup__closing .you { color: var(--magenta); }
  .rollup__stripe { position: absolute; left: 0; bottom: 0; width: 100%; height: 14px; background: linear-gradient(90deg, var(--blush), #e7a9cf); }

  .features { margin: 28px 0 0 10px; font-size: 14.5px; line-height: 1.2; white-space: nowrap; }
  .features li { list-style: none; }
  .features .f1 { color: var(--sky); font-size: 16px; }
  .features .f2 { color: var(--magenta); font-size: 12.5px; }
  .features .f3 { color: var(--coral); }
  .features .f4 { color: var(--ink); }
  .rollup__illustration {
    position: absolute; left: 0; bottom: 0; width: 100%; height: 330px;
    background: linear-gradient(180deg, rgba(126,58,158,.25) 0%, #5a2d8a 45%, #2f1f5a 100%);
  }

  /* Table skirt */
  .table-skirt { position: absolute; left: 330px; top: 580px; width: 540px; height: 200px; display: flex; }
  .table-skirt__front { position: relative; width: 390px; height: 100%; background: var(--panel-white); overflow: hidden; }
  .table-skirt__front .brand { position: relative; margin-top: 50px; }
  .table-skirt__front .brand__name { font-size: 62px; }
  .table-skirt__front .brand__sub { font-size: 24px; margin-top: 4px; }
  .table-skirt__art {
    position: absolute; left: 0; bottom: 0; width: 100%; height: 50px;
    background: linear-gradient(180deg, rgba(242,214,230,0) 0%, rgba(231,169,207,.55) 100%);
  }
  .table-skirt__side { width: 150px; height: 100%; background: linear-gradient(160deg, var(--magenta) 0%, var(--purple) 100%); }
</style>
</head>
<body>

  <aside class="rollup rollup--left">
    <div class="brand"><span class="brand__name">Volari</span><span class="brand__sub">collection</span></div>
    <div class="rollup__swirl" role="img" aria-label="Soft pink swirling line decoration"></div>
    <div class="rollup__product" role="img" aria-label="Photo of interchangeable snap bracelet"></div>
    <p class="rollup__note">interchangable</p>
    <div class="rollup__circles" role="img" aria-label="Faint pink circle decoration"></div>
    <p class="rollup__closing">
      <span class="small">CREATE YOUR OWN STYLE</span>
      <span class="big">DESIGNED BY <span class="you">YOU</span></span>
    </p>
    <div class="rollup__stripe"></div>
  </aside>

  <section class="backdrop">
    <div class="backdrop__art" role="img" aria-label="Pink and peach floral swirl artwork with circles"></div>
    <div class="brand"><span class="brand__name">Volari</span><span class="brand__sub">collection</span></div>
    <h1 class="tagline">
      <span class="tagline__lead">EXPRESS</span>
      <span class="tagline__rest">YOUR <span class="tagline__accent">INDIVIDUALITY</span></span>
    </h1>
  </section>

  <aside class="rollup rollup--right">
    <div class="brand"><span class="brand__name">Volari</span><span class="brand__sub">collection</span></div>
    <ul class="features">
      <li class="f1">Interchangeable</li>
      <li class="f2">Create your own style</li>
      <li class="f3">Designed by you</li>
      <li class="f4">Endless possibilities</li>
    </ul>
    <div class="rollup__illustration" role="img" aria-label="Illustration of a woman in profile with colourful butterflies in her hair"></div>
  </aside>

  <section class="table-skirt">
    <div class="table-skirt__front">
      <div class="table-skirt__art" role="img" aria-label="Soft pink swirl artwork along the lower edge"></div>
      <div class="brand"><span class="brand__name">Volari</span><span class="brand__sub">collection</span></div>
    </div>
    <div class="table-skirt__side"></div>
  </section>

</body>
</html>
```